Web design for Frostwerkly.com

We need a website (4 starter pages) designed for a drupal based site. The theme is flexible so I am open to different designs/looks. I am looking for a VERY simple and clean and FUN design to make it easy to use for the customer.

Our company is similar to Pitch lantern as in it's for multiple people to design a cake for a customer and they choose a winning design and work with that cake designer to make the cake (birthday, wedding etc...)

Our vision:
First page:
2 main images for either the customer to submit an idea for a cake, or the new designer to sign up to the site. Perhaps a mouse-over with wording on what the options are? You can use this site:
http://www.plumwidget.example/ as a sort of template but more clean and simple

"How it works" page:
Similar to this:
http://www.plumwidget.example/how-it-works
Fun, clean and simple

Submit cake design page (form submission)

Submit new designer page

Ideally a 960 wide design with no flash, but open to a flash design if it stands out...

Please contact me if you have any questions!

Target Market(s)

People who want a custom cake made, and people who design and make cakes.

Industry/Entity Type

Wedding

Requirements
Must have
• Use the logo attached. The "Tater Bop" should be a big part of the site...kind of a site mascot?
Nice to have
• 960 wide
No flash but not a deal-breaker if there is flash and it's amazing...

```html
<!DOCTYPE html>
<html lang="en">
<head>
<meta charset="utf-8">
<title>Frostwerkly.com</title>
<link rel="stylesheet" href="https://fonts.googleapis.com/css2?family=Lobster&family=Lora:ital@1&family=Ubuntu:wght@400;700&display=swap">
<style>
  :root {
    --cream: #f2ebe4;
    --brown: #5c4338;
    --brown-dark: #4a342b;
    --pink: #e8a3b4;
    --pink-band: #e3b2bd;
    --pink-panel: #ecd3d5;
    --pink-text: #f2a7b8;
    --orange-1: #ffd6a6;
    --orange-2: #fbb571;
    --green-1: #e2f2b8;
    --green-2: #bfe07a;
    --white: #ffffff;
    --taupe: #b9a88f;
    --caption: #6d5a52;
  }
  * { box-sizing: border-box; margin: 0; padding: 0; }
  html, body { width: 1200px; height: 960px; overflow: hidden; }
  body { position: relative; background: var(--cream); font-family: "Ubuntu", sans-serif; color: var(--brown); }

  .top-band { position: absolute; top: 0; left: 0; width: 1200px; height: 26px; background: linear-gradient(var(--pink-band), #ebc8ce); }

  .logo { position: absolute; left: 150px; top: 62px; display: flex; align-items: center; gap: 10px; }
  .logo-mark { width: 28px; height: 28px; border-radius: 50%; background: var(--pink); }
  .logo-name { font-family: "Ubuntu", sans-serif; font-weight: 700; font-size: 34px; color: var(--brown); letter-spacing: -0.5px; }

  .main-nav { position: absolute; left: 469px; top: 58px; width: 581px; height: 50px; }
  .nav-ribbon-end { position: absolute; top: 8px; width: 50px; height: 44px; background: #e6c3c8; }
  .nav-ribbon-end.left { left: 0; clip-path: polygon(0 0, 100% 0, 100% 100%, 0 100%, 22% 50%); }
  .nav-ribbon-end.right { right: 0; clip-path: polygon(0 0, 100% 0, 78% 50%, 100% 100%, 0 100%); }
  .nav-band { position: absolute; left: 28px; right: 28px; top: 0; height: 46px; background: linear-gradient(#f6dfe2, #eac4ca); border: 1px solid #f8e6e8; box-shadow: 0 2px 3px rgba(120,70,70,.18); display: flex; justify-content: space-around; align-items: center; padding: 0 16px; }
  .main-nav a { font-family: "Lobster", cursive; font-size: 17px; color: var(--brown); text-decoration: none; }

  .slider { position: absolute; left: 150px; top: 140px; width: 900px; height: 385px; }
  .photo-back { position: absolute; background: var(--white); box-shadow: 0 1px 4px rgba(90,60,50,.25); }
  .photo-back.one { left: 14px; top: 2px; width: 872px; height: 370px; transform: rotate(-0.9deg); }
  .photo-back.two { left: -8px; top: 20px; width: 916px; height: 340px; transform: rotate(0.6deg); }
  .photo-front { position: absolute; left: 0; top: 10px; width: 900px; height: 355px; background: var(--white); padding: 8px; box-shadow: 0 2px 5px rgba(90,60,50,.25); }
  .slide-art { position: relative; width: 100%; height: 100%; background: linear-gradient(135deg, #f3cfd8 0%, #f8f5f2 40%, #f8f5f2 60%, #ecaabb 100%); overflow: hidden; }
  .bubble { position: absolute; top: 43px; width: 272px; height: 66px; border-radius: 12px; text-align: center; box-shadow: 0 2px 3px rgba(100,70,50,.2); }
  .bubble::after { content: ""; position: absolute; left: 50%; bottom: -8px; margin-left: -8px; width: 16px; height: 16px; transform: rotate(45deg); background: inherit; }
  .bubble.customer { left: 80px; background: linear-gradient(var(--orange-1), var(--orange-2)); }
  .bubble.designer { left: 540px; background: linear-gradient(var(--green-1), var(--green-2)); }
  .bubble h2 { font-family: "Lobster", cursive; font-weight: 400; font-size: 24px; line-height: 1; padding-top: 9px; color: var(--brown); }
  .bubble p { font-family: "Lora", serif; font-style: italic; font-size: 15px; color: var(--brown); }
  .art-cake { position: absolute; top: 130px; height: 200px; border-radius: 50% 50% 12px 12px; }
  .art-cake.search { left: 10px; width: 330px; background: radial-gradient(circle at 60% 50%, #ffffff 0%, #e9e7e5 55%, rgba(240,140,80,.25) 100%); }
  .art-cake.paint { left: 605px; width: 330px; background: radial-gradient(circle at 45% 50%, #a8d24a 0%, #c7e38c 45%, rgba(240,240,240,.6) 100%); }

  .slide-arrow { position: absolute; top: 307px; width: 56px; height: 56px; border-radius: 50%; background: radial-gradient(#d2c4ae, var(--taupe)); border: 2px dashed #e8dfcf; display: flex; align-items: center; justify-content: center; box-shadow: 0 2px 4px rgba(80,60,40,.3); }
  .slide-arrow.prev { left: 122px; }
  .slide-arrow.next { left: 1022px; }

  .how-it-works { position: absolute; left: 150px; top: 568px; width: 900px; height: 220px; background: var(--pink-panel); border: 1px solid #f7ecec; }
  .section-tab { position: absolute; left: 309px; top: -24px; width: 282px; height: 49px; background: linear-gradient(#f1c5ce, #e3a6b3); border-radius: 8px; display: flex; align-items: center; justify-content: center; box-shadow: 0 2px 3px rgba(120,60,70,.2); }
  .section-tab::before, .section-tab::after { content: ""; position: absolute; top: 14px; width: 20px; height: 20px; background: #e6b0bb; transform: rotate(45deg); z-index: -1; }
  .section-tab::before { left: -8px; }
  .section-tab::after { right: -8px; }
  .section-tab h2 { font-family: "Lobster", cursive; font-weight: 400; font-size: 25px; color: var(--brown); text-shadow: 0 1px 0 rgba(255,255,255,.6); }
  .steps { position: absolute; left: 51px; top: 46px; display: flex; gap: 28px; }
  .step { width: 178px; text-align: center; }
  .step-image { width: 178px; height: 116px; border: 1px solid #dfaab3; background: #ecdfe0; display: flex; align-items: center; justify-content: center; }
  .step-image span { width: 116px; height: 82px; border-radius: 50% 50% 40% 40%; background: radial-gradient(circle at 50% 35%, #f3c63a 0%, #f0a33a 50%, #e88a2a 100%); }
  .step-caption { font-family: "Lora", serif; font-style: italic; font-size: 18px; color: var(--caption); margin-top: 10px; }
  .step-arrow { position: absolute; top: 80px; width: 37px; height: 57px; background: var(--brown-dark); display: flex; align-items: center; justify-content: center; }
  .step-arrow.prev { left: -1px; border-radius: 0 29px 29px 0; }
  .step-arrow.next { right: -1px; border-radius: 29px 0 0 29px; }

  .site-footer { position: absolute; left: 0; top: 826px; width: 1200px; height: 134px; background: var(--brown); }
  .newsletter { position: absolute; left: 152px; top: 30px; }
  .newsletter h3 { font-family: "Lobster", cursive; font-weight: 400; font-size: 24px; color: var(--white); }
  .newsletter-form { display: flex; gap: 10px; margin-top: 16px; }
  .newsletter-form .email { width: 229px; height: 29px; border: 1px solid #d8cfc8; background: var(--white); font-family: "Ubuntu", sans-serif; font-size: 13px; color: #333; padding: 0 9px; display: flex; align-items: center; }
  .newsletter-form .subscribe { width: 87px; height: 27px; margin-top: 1px; background: linear-gradient(#e69aa6, #cf7785); border: 1px solid #e9aab3; font-family: "Lobster", cursive; font-size: 14px; color: #8e3d4a; display: flex; align-items: center; justify-content: center; }
  .legal { position: absolute; right: 150px; top: 38px; text-align: right; font-size: 12px; color: var(--white); }
  .legal a { color: var(--pink-text); text-decoration: none; }
  .legal .links { margin-bottom: 20px; color: #e7d9d2; }
  .legal .copyright { line-height: 17px; }
</style>
</head>
<body>
  <div class="top-band" aria-hidden="true"></div>

  <header>
    <div class="logo">
      <span class="logo-mark"></span>
      <span class="logo-name">Frostwerkly.com</span>
    </div>
    <nav class="main-nav">
      <span class="nav-ribbon-end left"></span>
      <span class="nav-ribbon-end right"></span>
      <div class="nav-band">
        <a href="#">How it works</a>
        <a href="#">Sign Up</a>
        <a href="#">Log in</a>
        <a href="#">Help</a>
        <a href="#">Contact Us</a>
      </div>
    </nav>
  </header>

  <section class="slider">
    <div class="photo-back one"></div>
    <div class="photo-back two"></div>
    <div class="photo-front">
      <div class="slide-art" role="img" aria-label="Pink gingham backdrop with clouds">
        <div class="art-cake search" role="img" aria-label="White cake with orange roses and a magnifying glass"></div>
        <div class="art-cake paint" role="img" aria-label="Green tiered cake with white flowers and a paintbrush"></div>
        <div class="bubble customer">
          <h2>Looking for a custom cake?</h2>
          <p>Start to post a task here</p>
        </div>
        <div class="bubble designer">
          <h2>Are you a designer</h2>
          <p>Login or sign-up here</p>
        </div>
      </div>
    </div>
  </section>
  <span class="slide-arrow prev"><svg width="18" height="22" viewBox="0 0 18 22"><path d="M14 2 L4 11 L14 20" fill="none" stroke="#8f7e68" stroke-width="5" stroke-linecap="round" stroke-linejoin="round"/></svg></span>
  <span class="slide-arrow next"><svg width="18" height="22" viewBox="0 0 18 22"><path d="M4 2 L14 11 L4 20" fill="none" stroke="#8f7e68" stroke-width="5" stroke-linecap="round" stroke-linejoin="round"/></svg></span>

  <section class="how-it-works">
    <div class="section-tab"><h2>How it works</h2></div>
    <span class="step-arrow prev"><svg width="14" height="20" viewBox="0 0 14 20"><path d="M11 2 L3 10 L11 18" fill="none" stroke="#f1c3cc" stroke-width="4" stroke-linecap="round" stroke-linejoin="round"/></svg></span>
    <div class="steps">
      <div class="step"><div class="step-image" role="img" aria-label="Fruit tart with strawberries, kiwi and orange"><span></span></div><p class="step-caption">tutti fruity pie</p></div>
      <div class="step"><div class="step-image" role="img" aria-label="Fruit tart with strawberries, kiwi and orange"><span></span></div><p class="step-caption">tutti fruity pie</p></div>
      <div class="step"><div class="step-image" role="img" aria-label="Fruit tart with strawberries, kiwi and orange"><span></span></div><p class="step-caption">tutti fruity pie</p></div>
      <div class="step"><div class="step-image" role="img" aria-label="Fruit tart with strawberries, kiwi and orange"><span></span></div><p class="step-caption">tutti fruity pie</p></div>
    </div>
    <span class="step-arrow next"><svg width="14" height="20" viewBox="0 0 14 20"><path d="M3 2 L11 10 L3 18" fill="none" stroke="#f1c3cc" stroke-width="4" stroke-linecap="round" stroke-linejoin="round"/></svg></span>
  </section>

  <footer class="site-footer">
    <div class="newsletter">
      <h3>Get Update to Our Newsletter</h3>
      <div class="newsletter-form">
        <span class="email">E-mail</span>
        <span class="subscribe">SUBSCRIBE</span>
      </div>
    </div>
    <div class="legal">
      <p class="links"><a href="#">Terms &amp; Conditions</a> &nbsp;|&nbsp; <a href="#">Privacy Policy</a></p>
      <p class="copyright">Copyright © 2012 <a href="#">Frostwerkly</a>. All Rights Reserved</p>
    </div>
  </footer>
</body>
</html>
```